Healthy living company needs logo / business card

We are looking for a business identity for our company that operates in the Health and Wellness area.
Our audience is those open to hearing about the links between ill health and chemicals in the home as well as how to boost their health naturally through nutrition. We show people how to eliminate those toxins and share the message with others.
We also work with and mentor people who want to build their own business, share the message and create a leveraged income.
Our business name is: Brivora
The tag line we have is: Simple Changes ยท Healthy Living
Output for the project is:
Logo and business card design (2 people on the card).
Our perspective is for a modern, natural, simple, clean design (web 2.0 feel) that will appeal to a broad age range and audience. It should feel professional but not formal. It should not seem medical.
The logo should not be a gradient nor overly complex. Colouring should only be one or two colours at most. They can be bright, we are tending to lean towards green for obvious reasons but open to your thoughts.
Simplicity is the key.
The business card needs to be two sided. We like having the logo and card details on the front and then reversed out on the back with the logo and name in white on the colour block.
Please see the attached card brief document about the card content.

```html
<!DOCTYPE html>
<html lang="en">
<head>
<meta charset="utf-8">
<title>Brivora business card – front and back</title>
<link rel="stylesheet" href="https://fonts.googleapis.com/css2?family=Fira+Sans:wght@300;500;600&family=Fira+Sans+Condensed:wght@600&display=swap">
<style>
  :root {
    --leaf-green: #46b544;
    --paper: #ffffff;
    --card-edge: #d9d9d9;
  }
  * { margin: 0; padding: 0; box-sizing: border-box; }
  html, body {
    width: 1200px;
    height: 960px;
    overflow: hidden;
    background: var(--paper);
  }
  .canvas {
    position: relative;
    width: 1200px;
    height: 960px;
  }
  .card {
    position: absolute;
    left: 286px;
    width: 758px;
    height: 434px;
  }
  .card--front {
    top: 16px;
    background: var(--paper);
    border: 2px solid var(--card-edge);
    color: var(--leaf-green);
  }
  .card--back {
    top: 506px;
    background: var(--leaf-green);
    color: var(--paper);
  }
  .brand {
    position: absolute;
    display: flex;
    align-items: center;
    gap: 22px;
    font-family: "Fira Sans", sans-serif;
    font-weight: 500;
    line-height: 1;
    letter-spacing: -1px;
  }
  .brand__dot {
    border-radius: 50%;
    background: currentColor;
  }
  .card--front .brand { left: 52px; top: 46px; font-size: 96px; }
  .card--front .brand__dot { width: 56px; height: 56px; }
  .card--back .brand { left: 30px; top: 28px; font-size: 80px; }
  .card--back .brand__dot { width: 46px; height: 46px; }

  .tagline {
    position: absolute;
    font-family: "Fira Sans Condensed", sans-serif;
    font-weight: 600;
    line-height: 1;
    white-space: nowrap;
    letter-spacing: -0.5px;
  }
  .card--front .tagline { left: 52px; top: 166px; font-size: 44px; }
  .card--back .tagline { left: 30px; top: 128px; font-size: 38px; }

  .contact {
    position: absolute;
    top: 256px;
    font-family: "Fira Sans", sans-serif;
    font-weight: 600;
    font-size: 26px;
    line-height: 32px;
    list-style: none;
  }
  .contact--people { left: 50px; }
  .contact--people .person + .person { margin-top: 10px; }
  .contact--reach { left: 378px; line-height: 33px; }

  .aspirations {
    position: absolute;
    right: 32px;
    top: 84px;
    list-style: none;
    text-align: right;
    font-family: "Fira Sans", sans-serif;
    font-weight: 300;
    font-size: 24px;
    line-height: 32.6px;
    letter-spacing: 0.5px;
  }
</style>
</head>
<body>
<main class="canvas">
  <section class="card card--front" aria-label="Business card front">
    <div class="brand"><span class="brand__name">Brivora</span><span class="brand__dot"></span></div>
    <p class="tagline">simple changes • healthy living</p>
    <div class="contact contact--people">
      <p class="person">Name Name<br>465.210.4378</p>
      <p class="person">Name Name<br>501.733.6084</p>
    </div>
    <p class="contact contact--reach">emailaddress@email.com<br>451.640.2297<br>livebrivora.com</p>
  </section>

  <section class="card card--back" aria-label="Business card back">
    <div class="brand"><span class="brand__name">Brivora</span><span class="brand__dot"></span></div>
    <p class="tagline">simple changes • healthy living</p>
    <ul class="aspirations">
      <li>more time</li>
      <li>help others</li>
      <li>leave a legacy</li>
      <li>retirement plan</li>
      <li>health &amp; vitality</li>
      <li>meet new people</li>
      <li>financial freedom</li>
      <li>own my own business</li>
      <li>personal development</li>
      <li>multiple streams of income</li>
    </ul>
  </section>
</main>
</body>
</html>
```